Progressive Architecture and Urban Planning Studio - Stationery Design

The Kestrel Collective: a small boutique Architectural and Urban Planning Studio based in Natal/ RN, Brazil, about to open branches in South Africa and West Africa, established to provide high quality, innovative design and personal client service for projects worldwide. Our approach to Architecture: Minimal - Less is More, so to speak, but with an edge! Strive to produce "clean" projects - stripped of all that can be stripped, no excesses. Got our Logo right here with Pixel Harbor, and hope to do the same with our stationery (were informed that includes business cards, letterhead and envelopes). Since we'll be using two clour schemes, we want at least one using a black background (business card). We'll also allow manipulation of our logo if it helps the final design. Good Luck!

Font styles to use
Other font styles liked:
• Nexa

Colors

Designer to choose colors to be used in the design.

Requirements
Must have
• Business Cards/ Letterheads with the following address:
Rua Olavo Pereira 2741, Vale Dourado, Porto Claro/SE
Should be able to edit it.

```html
<!DOCTYPE html>
<html lang="en">
<head>
<meta charset="utf-8">
<title>The Kestrel Collective — Stationery</title>
<link href="https://fonts.googleapis.com/css2?family=Jost:wght@300;400;500&display=swap" rel="stylesheet">
<style>
  :root{
    --stage:#b8784c;
    --ink:#111111;
    --paper:#ffffff;
    --paper-shade:#ececec;
    --accent:#d71f26;
    --accent-faint:#f1d9d0;
    --text:#444444;
    --muted:#777777;
    --rule:#333333;
    --white:#ffffff;
  }
  *{box-sizing:border-box;margin:0;padding:0}
  html,body{width:1200px;height:393px;overflow:hidden}
  body{background:var(--stage);font-family:"Jost",sans-serif;color:var(--text);position:relative}

  .sheet{position:absolute;top:26px;width:248px;height:320px;
    background:linear-gradient(160deg,var(--paper) 40%,var(--paper-shade));
    box-shadow:0 1px 3px rgba(0,0,0,.35);overflow:hidden}
  .sheet--plain{left:26px}
  .sheet--address{left:298px}
  .sheet--fax{left:574px}
  .sheet-head{height:42px;background:var(--ink);position:relative}

  .wordmark{position:absolute;display:flex;flex-direction:column;align-items:center;gap:4px}
  .wordmark-square{width:10px;height:10px;background:var(--accent)}
  .wordmark-name{font-weight:400;color:var(--white);letter-spacing:.18em;text-transform:uppercase;white-space:nowrap}
  .sheet-head .wordmark{top:11px}
  .sheet--plain .sheet-head .wordmark{left:50%;transform:translateX(-50%)}
  .sheet--address .sheet-head .wordmark,.sheet--fax .sheet-head .wordmark{left:12px}
  .sheet-head .wordmark-name{font-size:5.6px}

  .watermark{position:absolute;top:150px;left:50%;transform:translateX(-50%);
    font-size:16px;font-weight:400;letter-spacing:.1em;color:var(--accent-faint);
    text-transform:uppercase;white-space:nowrap}

  .head-address{position:absolute;right:14px;top:12px;font-size:4.6px;line-height:1.5;color:#dddddd}
  .head-contacts{position:absolute;left:187px;top:8px;padding-left:5px;border-left:.5px solid #777;
    font-size:4.2px;line-height:1.55;color:#dddddd;list-style:none}

  .contact-line{display:flex;align-items:center;gap:2px;white-space:nowrap}
  .dot{display:inline-block;width:4px;height:4px;border-radius:50%;background:var(--accent);flex:none}

  .sheet-foot{position:absolute;left:0;right:0;bottom:6px;text-align:center;font-size:4.4px;color:var(--muted)}
  .sheet-foot .contact-row{display:flex;justify-content:center;gap:6px;margin-top:3px}

  .fax-title{position:absolute;left:14px;top:72px;font-size:16px;font-weight:400;color:var(--ink)}
  .fax-fields{position:absolute;left:12px;top:95px;width:213px;display:grid;
    grid-template-columns:110px 87px;column-gap:16px;row-gap:5px}
  .fax-field{font-size:4.4px;color:var(--text);border-bottom:.8px solid var(--rule);padding-bottom:2px;height:8px}
  .fax-checks{position:absolute;left:12px;top:156px;display:flex;gap:11px;font-size:4.4px;color:var(--text)}
  .fax-check{display:flex;align-items:center;gap:3px}
  .box{width:6px;height:6px;border:.8px solid var(--ink)}

  .option-label{position:absolute;top:356px;font-size:20px;font-weight:300;color:var(--white);transform:translateX(-50%)}

  .envelope{position:absolute;box-shadow:0 1px 3px rgba(0,0,0,.35);overflow:hidden}
  .envelope--back{left:902px;top:0;width:276px;height:140px;background:var(--paper)}
  .envelope--back svg{position:absolute;inset:0}
  .envelope--open{left:840px;top:68px;width:312px;height:124px;background:linear-gradient(180deg,var(--paper),var(--paper-shade))}
  .envelope--open svg{position:absolute;inset:0}
  .envelope--front{left:870px;top:124px;width:277px;height:123px;background:linear-gradient(160deg,var(--paper),var(--paper-shade))}
  .flap-mark{position:absolute;left:50%;transform:translateX(-50%);display:flex;flex-direction:column;align-items:center;gap:3px}
  .flap-mark .wordmark-name{font-size:4.6px}
  .envelope--back .flap-mark{top:28px}
  .envelope--open .flap-mark{top:14px}
  .envelope--open .wordmark-name{color:var(--ink)}
  .envelope-band{height:44px;background:var(--ink);position:relative}
  .envelope-band .wordmark{left:6px;top:8px;align-items:flex-start}
  .envelope-band .wordmark-name{font-size:5.6px}
  .envelope-address{position:absolute;left:6px;top:34px;font-size:4.2px;color:#dddddd}
  .envelope-web{position:absolute;left:6px;bottom:9px;font-size:4.6px;letter-spacing:.18em;color:var(--muted)}

  .card{position:absolute;top:268px;width:148px;height:84px;box-shadow:0 1px 3px rgba(0,0,0,.35)}
  .card--front{left:861px;background:var(--ink)}
  .card--back{left:1016px;background:var(--paper)}
  .card--front .wordmark{left:6px;top:24px;width:82px}
  .card--front .wordmark-name{font-size:5px;letter-spacing:.1em}
  .card-divider{position:absolute;left:89px;top:14px;width:.5px;height:56px;background:#666}
  .card-details{position:absolute;left:93px;top:14px;font-size:4.2px;line-height:1.5;color:#dddddd;list-style:none}
  .card-name{font-size:5.6px;color:var(--white)}
  .card-title{color:var(--accent);margin-bottom:3px}
  .card-address{margin-top:3px}
  .card--back .wordmark{left:50%;top:18px;transform:translateX(-50%);gap:6px}
  .card--back .wordmark-square{width:26px;height:26px}
  .card--back .wordmark-name{color:var(--ink);font-size:5.2px}
  .card-web{position:absolute;left:0;right:0;bottom:9px;text-align:center;font-size:4.4px;letter-spacing:.18em;color:var(--muted)}
</style>
</head>
<body>

  <section class="sheet sheet--plain" aria-label="Letterhead option 1">
    <header class="sheet-head">
      <div class="wordmark"><span class="wordmark-square"></span><span class="wordmark-name">The Kestrel Collective</span></div>
    </header>
    <div class="watermark">The Kestrel Collective</div>
    <footer class="sheet-foot">
      <div>Rua Olavo Pereira 2741, Vale Dourado, Porto Claro/SE</div>
      <div class="contact-row">
        <span class="contact-line"><span class="dot"></span>090-555-0147</span>
        <span class="contact-line"><span class="dot"></span>090-555-0148</span>
        <span class="contact-line"><span class="dot"></span>info@kestrelcollective.com</span>
        <span class="contact-line"><span class="dot"></span>www.kestrelcollective.com</span>
      </div>
    </footer>
  </section>

  <section class="sheet sheet--address" aria-label="Letterhead option 2">
    <header class="sheet-head">
      <div class="wordmark"><span class="wordmark-square"></span><span class="wordmark-name">The Kestrel Collective</span></div>
      <div class="head-address">Rua Olavo Pereira 2741<br>Vale Dourado, Porto Claro/SE</div>
    </header>
    <footer class="sheet-foot">
      <div class="contact-row">
        <span class="contact-line"><span class="dot"></span>090-555-0147</span>
        <span class="contact-line"><span class="dot"></span>090-555-0148</span>
        <span class="contact-line"><span class="dot"></span>info@kestrelcollective.com</span>
        <span class="contact-line"><span class="dot"></span>www.kestrelcollective.com</span>
      </div>
    </footer>
  </section>

  <section class="sheet sheet--fax" aria-label="Fax cover sheet">
    <header class="sheet-head">
      <div class="wordmark"><span class="wordmark-square"></span><span class="wordmark-name">The Kestrel Collective</span></div>
      <ul class="head-contacts">
        <li class="contact-line"><span class="dot"></span>090-555-0147</li>
        <li class="contact-line"><span class="dot"></span>090-555-0148</li>
        <li class="contact-line"><span class="dot"></span>info@kestrelcollective.com</li>
        <li class="contact-line"><span class="dot"></span>www.kestrelcollective.com</li>
      </ul>
    </header>
    <h1 class="fax-title">FAX</h1>
    <div class="fax-fields">
      <div class="fax-field">To :</div><div class="fax-field">From :</div>
      <div class="fax-field">Fax :</div><div class="fax-field">Pages :</div>
      <div class="fax-field">Phone :</div><div class="fax-field">Date :</div>
      <div class="fax-field">Re :</div><div class="fax-field">CC :</div>
    </div>
    <div class="fax-checks">
      <span class="fax-check"><span class="box"></span>Urgent</span>
      <span class="fax-check"><span class="box"></span>For Review</span>
      <span class="fax-check"><span class="box"></span>Please Comment</span>
      <span class="fax-check"><span class="box"></span>Please Reply</span>
      <span class="fax-check"><span class="box"></span>Please Recycle</span>
    </div>
    <footer class="sheet-foot">Rua Olavo Pereira 2741, Vale Dourado, Porto Claro/SE</footer>
  </section>

  <div class="option-label" style="left:144px">Option-1</div>
  <div class="option-label" style="left:416px">Option-2</div>
  <div class="option-label" style="left:690px">Option-3</div>

  <section class="envelope envelope--back" aria-label="Envelope back with black flap">
    <svg width="276" height="140" viewBox="0 0 276 140" aria-hidden="true">
      <path d="M0 0 H276 V30 Q264 36 220 56 L152 80 Q138 85 124 80 L56 56 Q12 36 0 30 Z" fill="var(--ink)"/>
    </svg>
    <div class="flap-mark"><span class="wordmark-square"></span><span class="wordmark-name">The Kestrel Collective</span></div>
  </section>

  <section class="envelope envelope--open" aria-label="Envelope back with white flap">
    <svg width="312" height="124" viewBox="0 0 312 124" aria-hidden="true">
      <path d="M0 10 Q6 8 26 14 L150 46 Q156 48 162 46 L286 14 Q306 8 312 10" fill="none" stroke="var(--ink)" stroke-width="1"/>
    </svg>
    <div class="flap-mark"><span class="wordmark-square"></span><span class="wordmark-name">The Kestrel Collective</span></div>
  </section>

  <section class="envelope envelope--front" aria-label="Envelope front">
    <div class="envelope-band">
      <div class="wordmark"><span class="wordmark-square"></span><span class="wordmark-name">The Kestrel Collective</span></div>
      <div class="envelope-address">Rua Olavo Pereira 2741, Vale Dourado, Porto Claro/SE</div>
    </div>
    <div class="envelope-web">www.kestrelcollective.com</div>
  </section>

  <section class="card card--front" aria-label="Business card front">
    <div class="wordmark"><span class="wordmark-square"></span><span class="wordmark-name">The Kestrel Collective</span></div>
    <span class="card-divider"></span>
    <ul class="card-details">
      <li class="card-name">Your Name</li>
      <li class="card-title">Title</li>
      <li class="contact-line"><span class="dot"></span>090-555-0147</li>
      <li class="contact-line"><span class="dot"></span>090-555-0148</li>
      <li class="contact-line"><span class="dot"></span>info@kestrelcollective.com</li>
      <li class="contact-line"><span class="dot"></span>www.kestrelcollective.com</li>
      <li class="card-address">Rua Olavo Pereira 2741<br>Vale Dourado, Porto Claro/SE</li>
    </ul>
  </section>

  <section class="card card--back" aria-label="Business card back">
    <div class="wordmark"><span class="wordmark-square"></span><span class="wordmark-name">The Kestrel Collective</span></div>
    <div class="card-web">www.kestrelcollective.com</div>
  </section>

</body>
</html>
```